Tamarind Crest Management - Business Cards

I need business cards. My current logo was designed by a designer at this site and I very much like and am happy with the results. I would like a business card that is trendy, unique, current yet professional. I deal with high net worth clients daily

Target Market(s)

Out of state investors looking to get into the rental market in Ohio

Industry/Entity Type

Property Management, Consulting

Contact Information for Business Card

Name, Title (Chief Financial Officer) office phone number (347) 681-9072 website address tamcrestmgmt.example

Font styles to use
Sans Serif

Colors
0054AA
0677BA
7BADD7
CADEEF
E8F1F8
0094D4
00A9DD
6FCCEA
C7EBF8
E9F6FB
00AB8E
00BBA5
67D7C9
C6EFE9
E9F9F6

```html
<!DOCTYPE html>
<html lang="en">
<head>
<meta charset="utf-8">
<title>Tamarind Crest Management – Business Cards</title>
<link href="https://fonts.googleapis.com/css2?family=Montserrat:wght@500&family=Roboto:wght@400;700&family=Ubuntu:wght@500&display=swap" rel="stylesheet">
<style>
  :root{
    --backdrop:#2b2b2b;
    --navy:#1f2d50;
    --red:#b3242a;
    --silver:#c9c9cc;
    --white:#f2f2f2;
  }
  *{margin:0;padding:0;box-sizing:border-box}
  html,body{width:1200px;height:1138px;overflow:hidden;background:var(--backdrop)}
  .canvas{position:relative;width:1200px;height:1138px}
  .card{position:absolute;width:620px;height:376px;background:var(--navy);border-radius:14px;overflow:hidden}
  .card--front{left:274px;top:186px}
  .card--back{left:276px;top:607px}
  .brand-name{font-family:"Roboto",sans-serif;font-weight:700;color:var(--white);text-align:center;line-height:1.1;letter-spacing:.5px}
  .card--front .brand-name{position:absolute;left:0;right:0;top:128px;font-size:40px}
  .front-web{position:absolute;left:0;right:0;top:336px;text-align:center;font-family:"Montserrat",sans-serif;font-weight:500;font-size:15px;letter-spacing:5px;color:var(--white)}
  .card--back .brand-name{position:absolute;left:40px;width:260px;top:92px;font-size:30px}
  .wave{position:absolute;left:0;top:0}
  .person{position:absolute;right:26px;top:58px;text-align:right}
  .person__name{font-family:"Ubuntu",sans-serif;font-weight:500;font-size:25px;color:var(--red);line-height:1.2}
  .person__title{font-family:"Roboto",sans-serif;font-size:16px;color:var(--white)}
  .contacts{position:absolute;right:26px;top:257px;list-style:none;font-family:"Roboto",sans-serif;font-size:15.5px;color:var(--white)}
  .contacts li{display:flex;justify-content:flex-end;align-items:center;height:22.5px}
  .contacts svg{margin-left:14px;width:14px;height:14px;fill:var(--white)}
</style>
</head>
<body>
<main class="canvas">
  <section class="card card--front" aria-label="Card front">
    <div class="brand-name">Tamarind Crest<br>Management</div>
    <div class="front-web">www.tamcrestmgmt.example</div>
  </section>

  <section class="card card--back" aria-label="Card back">
    <svg class="wave" width="620" height="376" viewBox="0 0 620 376" aria-hidden="true">
      <path d="M0,296 C80,340 180,350 280,310 C400,260 480,172 620,172 L620,187 C500,190 420,262 320,302 C220,346 100,352 0,318 Z" fill="var(--silver)"/>
      <path d="M45,306 C140,330 240,325 310,296" fill="none" stroke="var(--silver)" stroke-width="2"/>
      <path d="M0,338 C100,362 220,352 320,302 C420,252 500,199 620,199 L620,376 L0,376 Z" fill="var(--red)"/>
    </svg>
    <div class="brand-name">Tamarind Crest<br>Management</div>
    <div class="person">
      <div class="person__name">Daniel Marsh</div>
      <div class="person__title">Chief Financial Officer</div>
    </div>
    <ul class="contacts">
      <li>(347) 681-9072<svg viewBox="0 0 16 16"><path d="M2,6 C2,3 14,3 14,6 L11,7 L10,5.5 L6,5.5 L5,7 Z M4,8 L12,8 L13,13 L3,13 Z"/></svg></li>
      <li>www.tamcrestmgmt.example<svg viewBox="0 0 16 16"><path d="M1,3 H15 V13 H1 Z M2,4.5 V12 H14 V4.5 L8,9 Z M2.5,4 L8,8 L13.5,4 Z" fill-rule="evenodd"/></svg></li>
      <li>info@tamcrestmgmt.example<svg viewBox="0 0 16 16"><circle cx="8" cy="8" r="6.5" fill="none" stroke="#f2f2f2" stroke-width="1.3"/><path d="M1.5,8 H14.5 M8,1.5 V14.5 M8,1.5 C4,5 4,11 8,14.5 M8,1.5 C12,5 12,11 8,14.5" fill="none" stroke="#f2f2f2" stroke-width="1"/></svg></li>
      <li>Bldg No. 0, Country State - 000000<svg viewBox="0 0 16 16"><path d="M8,1 C5,1 3,3.2 3,6 C3,9.5 8,15 8,15 C8,15 13,9.5 13,6 C13,3.2 11,1 8,1 Z M8,4 A2,2 0 1 0 8.01,4 Z" fill-rule="evenodd"/></svg></li>
    </ul>
  </section>
</main>
</body>
</html>
```